Velunox clinic Website for young modern clinic

Website for velunox clinic
To be modern and sleek.
Clinic base - are young and modern.
Images
Main treatments are Velunox and lip enhancement
Needs to include
Link to Chatterpage
Link to quibbler
Price list
Room for a small brief on each item
Hours
Mon 10-4pm
Tues 10-4pm
Wed 12-8pm
Thurs Penwick Lane 0700-4pm
Friday 10- 2pm
Saturday 9am - 2pm
Booking page/calender
Where we are - map
Address:
52 Marlow Crescent, 4 Thornbury Parade KT9 3QW
Phone number 0208 743 9182 or 07931584027
Company Name: PMV
Address: 52 Marlow Crescent, 4 Thornbury Parade, KT9 3QW
Phone: 0208 743 9182
Website: www.poppymervynvisage.co.uk
Industry/Entity Type
Clinic
Number of Pages Required
3 page
Look and feel

```html
<!DOCTYPE html>
<html lang="en">
<head>
<meta charset="utf-8">
<title>Poppy Mervyn Visage</title>
<link rel="stylesheet" href="https://fonts.googleapis.com/css2?family=Lato:wght@400;700&family=Open+Sans:wght@400;600&display=swap">
<style>
:root{
  --ink:#111;
  --black:#000;
  --white:#fff;
  --paper:#f3f1f2;
  --line:#d9d9d9;
  --grey:#8a8a8a;
  --booking:#262424;
  --panel:rgba(40,38,38,.82);
  --footer:#141414;
  --map:#1c1c1c;
  --skin:#c9a999;
  --skin-dark:#8e6f66;
  --lip:#b97a82;
}
*{box-sizing:border-box;margin:0;padding:0}
html,body{width:669px;height:1200px;overflow:hidden;background:var(--white)}
body{position:relative;font-family:"Open Sans",Arial,sans-serif;color:var(--ink)}
.abs{position:absolute}
svg{display:block}

/* header */
.topstrip{left:0;top:0;width:669px;height:34px;background:var(--paper)}
.brand{left:27px;top:0;width:104px;height:83px;background:var(--white);display:flex;flex-direction:column;align-items:center;justify-content:center;gap:3px}
.brand-mark{font-family:"Lato",sans-serif;font-weight:700;font-size:14px;letter-spacing:1px;color:var(--ink);display:flex;align-items:center;gap:4px}
.brand-mark::before{content:"";width:8px;height:8px;border-radius:50%;background:var(--ink)}
.brand-name{font-family:"Lato",sans-serif;font-weight:700;font-size:8.5px;letter-spacing:1px;text-align:center;line-height:1.2;color:var(--ink)}
.top-icon{top:8px;width:19px;height:19px;border:1px solid #bbb;border-radius:50%;display:flex;align-items:center;justify-content:center}
.top-icon.active{border-color:#444}
.search{left:434px;top:50px;width:207px;height:20px;border:1px solid var(--line);font-size:6.5px;color:#aaa;padding:5px 8px}
.search svg{position:absolute;right:6px;top:5px}

/* nav */
.nav{left:0;top:83px;width:669px;height:33px;background:var(--black)}
.nav a{position:absolute;top:13px;font-size:6.5px;color:var(--white);text-decoration:none;letter-spacing:.2px}
.nav-pointer{left:53px;top:26px;width:0;height:0;border-left:7px solid transparent;border-right:7px solid transparent;border-bottom:7px solid var(--white)}

/* hero */
.hero{left:0;top:116px;width:669px;height:277px;background:linear-gradient(100deg,#b8afab 0%,#d8c7bf 45%,#caa596 70%,#9d7f76 100%)}
.hero-panel{left:0;top:188px;width:421px;height:142px;background:var(--panel);clip-path:polygon(0 0,100% 0,93% 100%,0 100%)}
.hero-title{left:29px;top:205px;font-family:"Lato",sans-serif;font-size:31px;color:var(--white);font-weight:400}
.hero-text{left:29px;top:248px;width:370px;font-size:7.3px;line-height:1.5;color:#e8e8e8}
.btn-dark{left:29px;top:286px;width:74px;height:19px;background:var(--black);color:var(--white);font-size:6.5px;display:flex;align-items:center;justify-content:center}
.dot{top:371px;width:7px;height:7px;border-radius:50%;border:1px solid var(--white)}
.dot.on{background:var(--ink);border-color:var(--white)}

/* booking */
.booking{left:0;top:393px;width:669px;height:61px;background:var(--booking)}
.book-label{top:415px;font-family:"Lato",sans-serif;font-size:16px;color:var(--white)}
.date{top:412px;width:74px;height:26px;border:1px solid #5a5a5a;display:flex;align-items:center;color:var(--white);font-size:8px}
.date .cal{width:22px;height:100%;border-right:1px solid #5a5a5a;display:flex;align-items:center;justify-content:center;margin-right:8px}
.book-search{left:469px;top:411px;width:84px;height:28px;background:var(--white);border:1px solid #bbb;font-family:"Lato",sans-serif;font-size:11px;display:flex;align-items:center;justify-content:center;color:var(--ink)}

/* treatments */
.treatments{left:0;top:454px;width:669px;height:340px;background:linear-gradient(180deg,#7a6a66 0%,#5e5250 50%,#4a4241 100%)}
.card{left:26px;width:616px;height:136px;background:var(--black);display:flex}
.card-photo{position:relative;display:flex;align-items:center;justify-content:center;font-family:"Lato",sans-serif;font-weight:700;font-size:16px;color:var(--white);letter-spacing:.3px}
.card-copy{position:relative;font-size:6.3px;line-height:1.45;color:#eee}
.card-copy p{margin-bottom:9px}
.btn-outline{position:absolute;width:52px;height:20px;border:1px solid var(--white);color:var(--white);font-size:6.5px;display:flex;align-items:center;justify-content:center}

/* info footer */
.info{left:0;top:794px;width:669px;height:254px;background:var(--footer)}
.col-title{top:828px;font-family:"Lato",sans-serif;font-size:13px;color:var(--white)}
.col-rule{top:854px;height:0;border-top:1px dotted #888}
.about-sub{left:26px;top:864px;font-size:8.5px;color:var(--white)}
.about-img{left:27px;top:882px;width:180px;height:52px;background:linear-gradient(90deg,#e7d7ea,#f2e6f1 50%,#e4d3e7)}
.about-text{left:27px;top:963px;width:182px;font-size:6.3px;line-height:1.4;color:var(--white)}
.btn-white-outline{left:27px;top:1000px;width:61px;height:17px;border:1px solid #ccc;color:var(--white);font-size:6.3px;display:flex;align-items:center;justify-content:center}
.hours-lead{left:255px;top:869px;font-size:8.5px;color:var(--white)}
.hours{left:255px;top:892px;list-style:none;color:var(--white);font-size:8px}
.hours li{height:19px}
.hours b{font-family:"Lato",sans-serif;font-weight:700;font-size:10px}
.view-all{left:615px;top:858px;font-size:6px;color:var(--white)}
.news{left:459px;width:180px;height:52px;border-bottom:1px dotted #888;display:flex;align-items:flex-start;gap:8px;padding-top:6px}
.news-date{width:24px;text-align:center;font-family:"Lato",sans-serif;font-size:9px;color:var(--white);line-height:1.2}
.news-thumb{width:27px;height:27px;background:linear-gradient(135deg,#e9d7cf,#c9a999)}
.news-text{width:110px;font-size:6.3px;line-height:1.4;color:var(--white)}

/* contact band */
.contact{left:0;top:1048px;width:669px;height:106px;background:var(--map)}
.c-icon{width:20px;height:20px;border:1px solid #777;display:flex;align-items:center;justify-content:center}
.c-text{font-family:"Lato",sans-serif;font-size:11.5px;color:var(--white)}

/* bottom */
.bottom{left:0;top:1154px;width:669px;height:46px;background:var(--black);text-align:center}
.bottom-links{position:absolute;left:0;right:0;top:15px;font-size:6.3px;color:var(--white)}
.copyright{position:absolute;left:0;right:0;top:28px;font-size:5.5px;color:#999}
</style>
</head>
<body>

<!-- header -->
<div class="abs topstrip"></div>
<div class="abs brand">
  <div class="brand-mark">PMV</div>
  <div class="brand-name">POPPY MERVYN<br>VISAGE</div>
</div>

<div class="abs top-icon active" style="left:549px">
  <svg width="9" height="9" viewBox="0 0 10 10"><circle cx="5" cy="5" r="4" fill="none" stroke="#222" stroke-width="1.2"/><path d="M5 2.5V5h2" fill="none" stroke="#222" stroke-width="1"/></svg>
</div>
<div class="abs top-icon" style="left:573px">
  <svg width="9" height="9" viewBox="0 0 10 10"><path d="M2 1l2 2-1 1.5c.7 1.3 1.5 2.1 2.5 2.5L7 6l2 2-1.5 1.5C4.5 9 1 5.5.5 2.5z" fill="#999"/></svg>
</div>
<div class="abs top-icon" style="left:598px">
  <svg width="9" height="8" viewBox="0 0 10 8"><rect x=".5" y=".5" width="9" height="7" fill="none" stroke="#999"/><path d="M.5 .5L5 4.5 9.5 .5" fill="none" stroke="#999"/></svg>
</div>
<div class="abs top-icon" style="left:623px">
  <svg width="8" height="10" viewBox="0 0 8 10"><path d="M4 10S0 5.5 0 3.8A4 4 0 0 1 8 3.8C8 5.5 4 10 4 10z" fill="#999"/><circle cx="4" cy="3.8" r="1.4" fill="#fff"/></svg>
</div>

<div class="abs search">Search
  <svg width="8" height="8" viewBox="0 0 8 8"><circle cx="3.2" cy="3.2" r="2.5" fill="none" stroke="#aaa"/><path d="M5 5l2.5 2.5" stroke="#aaa"/></svg>
</div>

<!-- nav -->
<nav class="abs nav">
  <a style="left:50px">HOME</a>
  <a style="left:106px">ABOUT US</a>
  <a style="left:175px">OUR SERVICE</a>
  <a style="left:254px">WORKING HOUR</a>
  <a style="left:343px">LATEST NEWS</a>
  <a style="left:422px">TESTIMONIALS</a>
  <a style="left:506px">CONTACT US</a>
  <span class="abs nav-pointer"></span>
</nav>

<!-- hero -->
<div class="abs hero" role="img" aria-label="Photo of a woman receiving a facial aesthetic treatment"></div>
<div class="abs hero-panel"></div>
<h1 class="abs hero-title">Poppy Mervyn Visage</h1>
<p class="abs hero-text">Lorem ipsum dolor sit amet, consectetur adipiscing elit, sed do eiusmod tempor incididunt ut labore et dolore magna aliquaLorem ipsum dolor sit amet, consectetur adipiscing elit</p>
<div class="abs btn-dark">READ MORE</div>
<span class="abs dot" style="left:31px"></span>
<span class="abs dot on" style="left:42px"></span>
<span class="abs dot" style="left:53px"></span>

<!-- booking -->
<div class="abs booking"></div>
<span class="abs book-label" style="left:128px">From</span>
<div class="abs date" style="left:181px"><span class="cal"><svg width="9" height="9" viewBox="0 0 9 9"><rect x=".5" y="1.5" width="8" height="7" fill="none" stroke="#fff"/><path d="M.5 3.5h8M2.5 0v2M6.5 0v2M2 5h1M4 5h1M6 5h1M2 7h1M4 7h1" stroke="#fff"/></svg></span>Sep - 09</div>
<span class="abs book-label" style="left:308px">To</span>
<div class="abs date" style="left:342px"><span class="cal"><svg width="9" height="9" viewBox="0 0 9 9"><rect x=".5" y="1.5" width="8" height="7" fill="none" stroke="#fff"/><path d="M.5 3.5h8M2.5 0v2M6.5 0v2M2 5h1M4 5h1M6 5h1M2 7h1M4 7h1" stroke="#fff"/></svg></span>Sep - 09</div>
<div class="abs book-search">SEARCH</div>

<!-- treatments -->
<div class="abs treatments" role="img" aria-label="Soft blurred clinic photograph behind the treatment cards"></div>

<div class="abs card" style="top:485px">
  <div class="card-photo" style="width:262px;background:linear-gradient(135deg,#d9c3b9,var(--skin) 55%,var(--skin-dark))" role="img" aria-label="Photo of a Velunox injection to the forehead">VELUNOX</div>
  <div class="card-copy" style="width:354px;padding:24px 36px 0 54px">
    <p>Lorem ipsum dolor sit amet, consectetur adipiscing elit, sed do eiusmod tempor incididunt ut labore et dolore magna aliqua. Ut enim ad minim veniam, quis nostrud exercitation ullamco laboris nisi ut aliquip ex ea commodo consequat.</p>
    <p>Lorem ipsum dolor sit amet, consectetur adipiscing elit, sed do eiusmod tempor incididunt ut labore et dolore magna aliqua. Ut enim ad minim veniam, quis nostrud exercitation ullamco laboris nisi ut aliquip ex ea commodo consequat.</p>
    <div class="btn-outline" style="left:54px;top:100px">Read More</div>
  </div>
</div>

<div class="abs card" style="top:638px">
  <div class="card-copy" style="width:360px;padding:30px 26px 0 32px;text-align:right">
    <p>Lorem ipsum dolor sit amet, consectetur adipiscing elit, sed do eiusmod tempor incididunt ut labore et dolore magna aliqua. Ut enim ad minim veniam, quis nostrud exercitation ullamco laboris nisi ut aliquip ex ea commodo consequat.</p>
    <p>Lorem ipsum dolor sit amet, consectetur adipiscing elit, sed do eiusmod tempor incididunt ut labore et dolore magna aliqua. Ut enim ad minim veniam, quis nostrud exercitation ullamco laboris nisi ut aliquip ex ea commodo consequat.</p>
    <div class="btn-outline" style="left:254px;top:101px">Read More</div>
  </div>
  <div class="card-photo" style="width:256px;background:linear-gradient(180deg,#c9a99e,var(--lip) 60%,#8f6a6c)" role="img" aria-label="Close-up photo of lips after lip enhancement">LIP ENHANCEMENT</div>
</div>

<!-- info footer -->
<div class="abs info"></div>

<h2 class="abs col-title" style="left:27px">About Us</h2>
<div class="abs col-rule" style="left:27px;width:174px"></div>
<p class="abs about-sub">Lorem ipsum dolor sit amet</p>
<div class="abs about-img" role="img" aria-label="Illustration of facial treatment areas with labels"></div>
<p class="abs about-text">Lorem ipsum dolor sit amet, consectetur adipiscing elit, sed do eiusmod tempor incididunt ut labore et dolore magna aliqua. Ut enim ad minim veniam</p>
<div class="abs btn-white-outline">READ MORE</div>

<h2 class="abs col-title" style="left:255px">Opening Hours</h2>
<div class="abs col-rule" style="left:255px;width:167px"></div>
<p class="abs hours-lead">We are open every day of the year.</p>
<ul class="abs hours">
  <li><b>Mon</b> &nbsp;- 10am - 4pm</li>
  <li><b>Tues</b> &nbsp;- 10am - 4pm</li>
  <li><b>Wed</b> &nbsp;- 12pm - 8pm</li>
  <li><b>Thurs Penwick Lane</b> &nbsp;- 07am - 4pm</li>
  <li><b>Friday</b> &nbsp;- &nbsp;10am - 2pm</li>
  <li><b>Saturday</b> &nbsp;- &nbsp;9am - 2pm</li>
</ul>

<h2 class="abs col-title" style="left:460px">Latest News</h2>
<div class="abs col-rule" style="left:459px;width:180px"></div>
<span class="abs view-all">View All</span>
<div class="abs news" style="top:868px">
  <div class="news-date">17<br>Aug</div>
  <div class="news-thumb" role="img" aria-label="News thumbnail photo"></div>
  <div class="news-text">Give up alcohol if cancer runs in your family, Halden study warns - The Southern Ledger</div>
</div>
<div class="abs news" style="top:920px">
  <div class="news-date">17<br>Aug</div>
  <div class="news-thumb" role="img" aria-label="News thumbnail photo"></div>
  <div class="news-text">Give up alcohol if cancer runs in your family, Halden study warns - The Southern Ledger</div>
</div>
<div class="abs news" style="top:972px">
  <div class="news-date">17<br>Aug</div>
  <div class="news-thumb" role="img" aria-label="News thumbnail photo"></div>
  <div class="news-text">Give up alcohol if cancer runs in your family, Halden study warns - The Southern Ledger</div>
</div>

<!-- contact band -->
<div class="abs contact" role="img" aria-label="Dark street map showing the clinic location"></div>
<div class="abs c-icon" style="left:53px;top:1076px"><svg width="10" height="10" viewBox="0 0 10 10"><path d="M2 1l2 2-1 1.5c.7 1.3 1.5 2.1 2.5 2.5L7 6l2 2-1.5 1.5C4.5 9 1 5.5.5 2.5z" fill="#fff"/></svg></div>
<span class="abs c-text" style="left:83px;top:1079px">+0208 743 9182</span>
<div class="abs c-icon" style="left:236px;top:1076px"><svg width="8" height="10" viewBox="0 0 8 10"><rect x=".5" y=".5" width="7" height="9" rx="1" fill="none" stroke="#fff"/><circle cx="4" cy="8" r=".7" fill="#fff"/></svg></div>
<span class="abs c-text" style="left:267px;top:1079px">+07931584027</span>
<div class="abs c-icon" style="left:428px;top:1076px"><svg width="10" height="8" viewBox="0 0 10 8"><rect x=".5" y=".5" width="9" height="7" fill="none" stroke="#fff"/><path d="M.5 .5L5 4.5 9.5 .5" fill="none" stroke="#fff"/></svg></div>
<span class="abs c-text" style="left:459px;top:1079px">info@poppymervynvisage.co.uk</span>
<div class="abs c-icon" style="left:53px;top:1107px"><svg width="8" height="10" viewBox="0 0 8 10"><path d="M4 10S0 5.5 0 3.8A4 4 0 0 1 8 3.8C8 5.5 4 10 4 10z" fill="#fff"/><circle cx="4" cy="3.8" r="1.4" fill="#1c1c1c"/></svg></div>
<span class="abs c-text" style="left:84px;top:1110px;font-size:10.5px">52 Marlow Crescent, 4 Thornbury Parade KT9 3QW</span>

<!-- bottom -->
<footer class="abs bottom">
  <div class="bottom-links">Home &nbsp;/ &nbsp;About Us / &nbsp;Our Service &nbsp;/ &nbsp;Testimonials &nbsp;/ &nbsp;Latest News &nbsp;/ &nbsp;Working Hour &nbsp;/ &nbsp;Contact Us</div>
  <div class="copyright">Copyright 2015 Comapny name. All Rights Reserved.</div>
</footer>

</body>
</html>
```